Briarwood Homes Lakeshore Customer Brochure

Need a brochure designed that is clean and minimal that contains our logo, and contact information. Would like an area where we could insert business cards, and slips on both sides of the openings to place sheets of paper in. Would prefer to have the COVER LETTER I have attached printed on one side of the opening.

Target Market(s)

Home buyers

Font styles to use
Sans Serif

Colors

Designer to choose colors to be used in the design.

Requirements
Must have
• Logo, contact info, website, etc. Must be minimal in design and very clean looking.
Nice to have
• Please see above
Should not have
• No stock pictures of homes, builds, etc. Need it to look very clean

```html
<!DOCTYPE html>
<html lang="en">
<head>
<meta charset="utf-8">
<title>Briarwood Homes Lakeshore – Customer Brochure</title>
<link rel="stylesheet" href="https://fonts.googleapis.com/css2?family=Lato:wght@400;700&family=Roboto+Condensed:wght@300;700&display=swap">
<style>
  :root{
    --backdrop:#cccccc;
    --tan:#d2a87b;
    --tan-light:#e0c19c;
    --ink:#313131;
    --charcoal:#333333;
    --paper:#ffffff;
    --label:#222222;
  }
  *{box-sizing:border-box;margin:0;padding:0}
  html,body{width:1200px;height:1200px;overflow:hidden;background:var(--backdrop)}
  body{position:relative;font-family:"Lato",sans-serif;color:var(--ink)}

  .view-label{position:absolute;font-family:"Lato",sans-serif;font-size:29px;color:var(--label);white-space:nowrap;line-height:1}
  .view-label--front{left:214px;top:44px}
  .view-label--back{left:216px;top:620px}
  .view-label--inside{left:830px;top:620px}

  .sheet{position:absolute;background:var(--paper);overflow:hidden;box-shadow:4px 5px 6px rgba(0,0,0,.28)}
  .sheet--front{left:42px;top:102px;width:648px;height:462px}
  .sheet--back{left:43px;top:690px;width:648px;height:461px}
  .sheet--inside{left:811px;top:690px;width:328px;height:461px}

  .panel-tan{position:absolute;left:0;top:0;width:326px;height:100%;background:var(--tan)}
  .decor{position:absolute;left:0;top:0;width:100%;height:100%}

  /* brand name block (square + wordmark set in text) */
  .brand{position:absolute;display:flex;flex-direction:column;align-items:center;text-align:center}
  .brand__square{background:var(--charcoal)}
  .brand__name{font-family:"Roboto Condensed",sans-serif;font-weight:700;color:var(--charcoal);line-height:1;text-transform:uppercase}
  .brand--cover-left{left:0;width:326px;top:198px}
  .brand--cover-left .brand__square{width:46px;height:46px}
  .brand--cover-left .brand__name{font-size:12px;margin-top:8px}
  .brand--cover-left .brand__name + .brand__name{font-size:8px;letter-spacing:2.6px;margin-top:1px}

  .brand--cover{left:426px;width:192px;top:146px}
  .brand--cover .brand__square{width:73px;height:73px}
  .brand--cover .brand__name{font-size:19px;margin-top:10px}
  .brand--cover .brand__name + .brand__name{font-size:13px;letter-spacing:4px;margin-top:2px}
  .cover-url{font-size:7px;letter-spacing:1.4px;color:var(--ink);margin-top:8px}
  .cover-rule{width:75px;height:2px;background:var(--tan);margin-top:5px}

  .cover-backing{position:absolute;left:385px;top:98px;width:196px;height:196px;background:#fbfbfb}

  .contact-stack{position:absolute;left:0;width:326px;top:279px;display:flex;flex-direction:column;align-items:center;font-size:6.8px;font-weight:700;color:var(--paper);text-align:center}
  .contact-stack .icon{width:8px;height:8px;fill:var(--charcoal);margin-bottom:2px}
  .contact-stack span{display:block;margin-bottom:7px;line-height:1.1}
  .social-row{display:flex;gap:12px;margin-top:8px}
  .social-dot{width:12px;height:12px;border-radius:50%;background:var(--paper)}

  /* letter on back */
  .letter{position:absolute;left:24px;top:32px;width:284px;font-size:7.5px;line-height:9.95px;color:var(--paper);text-align:justify;hyphens:auto}
  .signoff{position:absolute;left:192px;top:283px;font-family:"Roboto Condensed",sans-serif;font-weight:700;font-size:8px;color:var(--charcoal);line-height:11px}
  .signoff p + p{margin-top:10px}
  .brand--letter{left:176px;width:51px;top:338px}
  .brand--letter .brand__square{width:23px;height:23px}
  .brand--letter .brand__name{font-size:5px;margin-top:3px}
  .brand--letter .brand__name + .brand__name{font-size:3.6px;letter-spacing:1.2px;margin-top:0}

  .contact-list{position:absolute;list-style:none}
  .contact-list li{display:flex;align-items:flex-start;gap:6px}
  .contact-list .icon{flex:none}
  .contact-list--back{left:174px;top:384px;font-size:6.6px;color:var(--paper);width:140px}
  .contact-list--back li{margin-bottom:7px;line-height:1.15}
  .contact-list--back .icon{width:6px;height:6px;fill:var(--charcoal);margin-top:1px}
  .contact-list--back li:last-child{font-weight:700}

  /* inside sheet */
  .brand--inside{left:0;width:328px;top:24px}
  .brand--inside .brand__square{width:42px;height:42px}
  .brand--inside .brand__name{font-size:10px;margin-top:6px}
  .brand--inside .brand__name + .brand__name{font-size:7px;letter-spacing:2px;margin-top:0}
  .profile-title{position:absolute;left:0;width:328px;top:101px;text-align:center;font-family:"Roboto Condensed",sans-serif;font-size:21px;color:var(--charcoal);line-height:1}
  .profile-title strong{font-weight:700}
  .profile-title span{font-weight:300}
  .salutation{position:absolute;left:22px;top:133px;font-family:"Roboto Condensed",sans-serif;font-weight:700;font-size:5.5px;color:var(--charcoal)}
  .profile-body{position:absolute;left:22px;top:147px;width:286px;font-size:5.2px;line-height:6.9px;color:var(--ink);text-align:justify}
  .contact-list--inside{left:22px;top:269px;font-size:4.8px;color:var(--ink)}
  .contact-list--inside li{margin-bottom:5.5px;line-height:1.2}
  .contact-list--inside .icon{width:5px;height:5px;fill:var(--charcoal)}
</style>
</head>
<body>

<svg width="0" height="0" style="position:absolute" aria-hidden="true">
  <defs>
    <symbol id="i-phone" viewBox="0 0 24 24"><path d="M6.6 10.8a15.1 15.1 0 0 0 6.6 6.6l2.2-2.2a1 1 0 0 1 1-.25 11.4 11.4 0 0 0 3.6.57 1 1 0 0 1 1 1V20a1 1 0 0 1-1 1A17 17 0 0 1 3 4a1 1 0 0 1 1-1h3.5a1 1 0 0 1 1 1c0 1.25.2 2.45.57 3.57a1 1 0 0 1-.25 1z"/></symbol>
    <symbol id="i-fax" viewBox="0 0 24 24"><path d="M6 2h12v6H6zM3 9h18a1 1 0 0 1 1 1v8h-4v4H6v-4H2v-8a1 1 0 0 1 1-1zm5 7v4h8v-4z"/></symbol>
    <symbol id="i-web" viewBox="0 0 24 24"><path d="M12 2a10 10 0 1 0 0 20 10 10 0 0 0 0-20zm0 2c.9 1.2 1.6 2.7 2 4.5h-4c.4-1.8 1.1-3.3 2-4.5zM4.3 10.5h4.1a17 17 0 0 0 0 3H4.3a8 8 0 0 1 0-3zm11.3 0h4.1a8 8 0 0 1 0 3h-4.1a17 17 0 0 0 0-3zm-5.2 0h3.2a15 15 0 0 1 0 3h-3.2a15 15 0 0 1 0-3zM10 15.5h4c-.4 1.8-1.1 3.3-2 4.5-.9-1.2-1.6-2.7-2-4.5z"/></symbol>
    <symbol id="i-mail" viewBox="0 0 24 24"><path d="M2 5h20v14H2zm2 2v.5l8 5 8-5V7zm0 2.9V17h16V9.9l-8 5z"/></symbol>
    <symbol id="i-pin" viewBox="0 0 24 24"><path d="M12 2a7 7 0 0 0-7 7c0 5 7 13 7 13s7-8 7-13a7 7 0 0 0-7-7zm0 9.5A2.5 2.5 0 1 1 12 6.5a2.5 2.5 0 0 1 0 5z"/></symbol>
  </defs>
</svg>

<p class="view-label view-label--front">front side of the brouchure</p>
<p class="view-label view-label--back">back side of the brouchure</p>
<p class="view-label view-label--inside">inside of the brouchure</p>

<!-- Front side -->
<section class="sheet sheet--front">
  <div class="panel-tan"></div>
  <svg class="decor" viewBox="0 0 648 462" aria-hidden="true">
    <polyline points="-4,120 133,50 133,-4" fill="none" stroke="var(--tan-light)" stroke-width="10"/>
    <polygon points="367,0 498,0 498,38 432,84 367,38" fill="var(--tan)"/>
    <polyline points="246,-2 246,26 329,91 414,26 414,-2" fill="none" stroke="var(--ink)" stroke-width="2"/>
    <polygon points="437,463 437,438 542,362 649,438 649,463" fill="var(--tan)"/>
    <polyline points="528,463 528,426 605,370 650,402" fill="none" stroke="var(--ink)" stroke-width="2"/>
  </svg>

  <div class="brand brand--cover-left">
    <div class="brand__square"></div>
    <p class="brand__name">Briarwood</p>
    <p class="brand__name">Homes</p>
  </div>

  <div class="contact-stack">
    <svg class="icon"><use href="#i-phone"/></svg><span>555-014-2381</span>
    <svg class="icon"><use href="#i-fax"/></svg><span>555-014-2390</span>
    <svg class="icon"><use href="#i-web"/></svg><span>www.briarwoodhomeslakeshore.com</span>
    <svg class="icon"><use href="#i-mail"/></svg><span>info@briarwoodhomeslakeshore.com</span>
    <svg class="icon"><use href="#i-pin"/></svg><span>48 HARBOURVIEW RD. PORT ELMSLEY, ONTARIO, K0H 2M0.</span>
    <div class="social-row"><span class="social-dot"></span><span class="social-dot"></span></div>
  </div>

  <div class="cover-backing"></div>
  <div class="brand brand--cover">
    <div class="brand__square"></div>
    <p class="brand__name">Briarwood</p>
    <p class="brand__name">Homes</p>
    <p class="cover-url">www.briarwoodhomeslakeshore.com</p>
    <div class="cover-rule"></div>
  </div>
</section>

<!-- Back side -->
<section class="sheet sheet--back">
  <div class="panel-tan"></div>
  <svg class="decor" viewBox="0 0 648 461" aria-hidden="true">
    <polygon points="32,462 32,422 93,380 155,422 155,462" fill="var(--tan-light)"/>
    <polyline points="-2,367 11,354 94,412 94,462" fill="none" stroke="var(--ink)" stroke-width="1.6"/>
    <path d="M325,462 V379 a45,45 0 0 1 45,-45 H649 V462 Z" fill="var(--charcoal)"/>
    <polygon points="509,334 649,334 649,378 589,422 509,382" fill="var(--tan)"/>
    <polyline points="569,333 569,370 629,414 649,400" fill="none" stroke="var(--paper)" stroke-width="2"/>
    <g stroke="var(--tan)" stroke-width="1">
      <line x1="358" y1="378" x2="368" y2="367"/>
      <line x1="478" y1="367" x2="487" y2="378"/>
      <line x1="358" y1="434" x2="368" y2="444"/>
      <line x1="477" y1="444" x2="487" y2="434"/>
    </g>
  </svg>

  <div class="letter">
    <p>Welcome to the new vision of home building in Lakeshore. For too long, the building and development business has been saddled with a poor image. Cost overruns, missed deadlines, and poor workmanship has led to most consumers feeling uneasy on building a new home. Unfortunately, in most cases, this image is warranted.</p>
    <p>When we started The Briarwood Group in 1992, we vowed do our utmost to dispel the industry of this negative rap. We wanted to make honesty, solid workmanship, and above all, excellent service our hallmarks.</p>
    <p>Quite often, the language used by builders to describe their homes can be difficult for consumers to understand. At Briarwood Homes, we value the opportunity to sit down with each and every client to explain any confusion terminology, as well as absorb as much input as we can from you, the purchaser. Furthermore, this ensures that there are no misconceptions or misunderstandings that exist between us and our clients before executing any contract. We go to great lengths to maintain our hallmarks and to ensure that we have nothing but satisfied customers.</p>
    <p>There couldn't be a better time to build a new home in the Lakeshore Region. Industries are booming, and the beautiful landscape this region has to offer has led to new citizens flocking down here in recent years. From the wineries and restaurants to the picturesque views and kind neighbors, the region of Lakeshore has become a desirable spot for families of all types.</p>
    <p>The time is now to make your dreams a reality. We look forward to the opportunity to build your dream home in the near future, and if you have any questions, please do not hesitate to ask myself, or a member of my staff.</p>
  </div>

  <div class="signoff">
    <p>Yours truly,</p>
    <p>Marco Bellanti<br>Founder and President</p>
  </div>

  <div class="brand brand--letter">
    <div class="brand__square"></div>
    <p class="brand__name">Briarwood</p>
    <p class="brand__name">Homes</p>
  </div>

  <ul class="contact-list contact-list--back">
    <li><svg class="icon"><use href="#i-phone"/></svg>555-014-2381</li>
    <li><svg class="icon"><use href="#i-fax"/></svg>555-014-2390</li>
    <li><svg class="icon"><use href="#i-web"/></svg>www.briarwoodhomeslakeshore.com</li>
    <li><svg class="icon"><use href="#i-pin"/></svg>48 HARBOURVIEW RD. PORT ELMSLEY, ONTARIO, K0H 2M0.</li>
  </ul>
</section>

<!-- Inside -->
<section class="sheet sheet--inside">
  <svg class="decor" viewBox="0 0 328 461" aria-hidden="true">
    <polygon points="0,462 0,434 166,350 329,422 329,462" fill="var(--tan)"/>
    <polyline points="198,462 198,402 294,331 330,355" fill="none" stroke="var(--ink)" stroke-width="1.4"/>
  </svg>

  <div class="brand brand--inside">
    <div class="brand__square"></div>
    <p class="brand__name">Briarwood</p>
    <p class="brand__name">Homes</p>
  </div>

  <h1 class="profile-title"><strong>Corporate</strong> <span>Profile</span></h1>
  <p class="salutation">Dear Sir/Madam:</p>

  <div class="profile-body">
    <p>At Briarwood Homes (Lakeshore), we believe that there is only one way to build a new home: with pride in one's craft and superior workmanship. Quality construction can be hard to find, and our staff works every day to change that. From starter homes to custom builds, we construct each house as if it were our own.</p>
    <p>We use only superior materials and employ first rate, dedicated trades to ensure that each house is given the utmost priority when it comes to quality. We take such care because we want to be proud of each home we build, just as proud as you will be living in it.</p>
    <p>Beginning in 1992 and stretching over two family generations, the Briarwood Group has left a quality product in nearly every corner of the Lakeshore Region. From our early work along the harbour to our recent projects inland, the results speak for themselves. Over the next few years, our endeavours will lead us into new towns where we will be pushing to create a new age of home building in the region.</p>
    <p>Building fine homes has been a passion that this family has kept for decades. You are encouraged to visit our website for more information about our current and future developments. It is here that you will find a wide range of elevations and floor plans that we keep updating to ensure that each client can find something that meets their tastes and needs.</p>
  </div>

  <ul class="contact-list contact-list--inside">
    <li><svg class="icon"><use href="#i-phone"/></svg>555-014-2381</li>
    <li><svg class="icon"><use href="#i-fax"/></svg>555-014-2390</li>
    <li><svg class="icon"><use href="#i-web"/></svg>www.briarwoodhomeslakeshore.com</li>
    <li><svg class="icon"><use href="#i-pin"/></svg>48 HARBOURVIEW RD. PORT ELMSLEY,<br>ONTARIO, K0H 2M0.</li>
  </ul>
</section>

</body>
</html>
```